Design for Retail Product - Resealable bag. Will also need a smaller version of the same.

DESIGN REQUIREMENTS:

- Design a 16 oz bag (approx. dimensions of 6.5" wide, by 8.5" high), that represents our unique nutritional salt.

- The design should be easily downsized to a correlating/proportionate version for a smaller 8 oz bag. (The 8oz bag may/or may not have a slightly different variation in design, but if a different design, must well alongside the 16 oz bag.) .

- If we can't fit all of the product info on the bag- we will decide what can be eliminated as we finalize designs.

- This bag will be capable of standing alone on a store shelf.

- The design color can be printed to the edges top and bottom, but we will lose approx an inch of the top of the bag (above the zipper), when the customer opens the bag.

- The design can be printed to within 1/4cm of the left and right hand edges of the bag.

- The design should convey some, but not necessarily all, of the following attributes: power, versatility, athletics, clean - as in pure/free of contaminants, nutrition, physical exertion, strength, hydration, determination.

- We use a lot of the color blue, as you see in our logo, but are open to other coordinating colors.

- There are two versions of our logo attached. One is vector but in white. I would like it to be blue as it is in the jpeg file.

- Also, there is a variety of text , that should be printed on the back of the package. It is included in the attached pdf so that you can gauge placement.

- A bar code will be printed on the bottom of the bag.

- The ingredients are of utmost importance - no color or image behind them, so that they are legible.

- You are designing a 16 oz bag, with a correlating/proportionate version for a smaller 8 oz bag. The 8oz bag may/or may not have a slightly different variation in design, but if a different design, must well alongside the 16 oz bag.

WHAT WE SELL:

- Our product, called Marrow Crest, can be used as a sports supplement (as an electrolyte replacement) and in cooking and baking.

- This will be a printed, zipper top bag, with a clear window somewhere on the front of the package, so that the customer can see what the salt looks like.

Target Market(s)

Athletes, Nutrition conscious individuals, Healthy lifestyle, Hydration

Requirements
Must have
• - Strong design element , outside of copy placement
• - Must have a window to see our product - and how it looks different than other salts on the market
• - Some kind of a blue, that coordinates well with our logo
• - Our ingredients must be very legible
Nice to have
• - Images on the package
• - more than one color, or have various shades/layers of a color
Should not have
• - not have the look or feel of a "spa"

```html
<!DOCTYPE html>
<html lang="en">
<head>
<meta charset="utf-8">
<title>Marrow Crest – 16 oz Bag Front</title>
<link rel="stylesheet" href="https://fonts.googleapis.com/css2?family=Jost:wght@300;400;700&family=Josefin+Sans:wght@400&display=swap">
<style>
  :root {
    --paper: #ffffff;
    --ink: #000000;
    --brand-blue: #03a9ce;
    --sky-blue: #7fb6ce;
    --signal-red: #be1e2e;
    --deep-navy: #053f6b;
    --night-violet: #27215f;
    --tagline-ink: #222222;
  }
  html, body {
    margin: 0;
    padding: 0;
    overflow: hidden;
    background: var(--paper);
  }
  .bag-front {
    position: relative;
    width: 918px;
    height: 1200px;
    overflow: hidden;
    background: var(--paper);
  }
  .bag-art {
    position: absolute;
    inset: 0;
    width: 918px;
    height: 1200px;
    display: block;
  }
  .badge-ring { fill: none; stroke: var(--ink); stroke-width: 3.2; }
  .badge-slash { stroke: var(--ink); stroke-width: 3.2; stroke-linecap: round; }
  .badge-label {
    font-family: "Jost", sans-serif;
    font-weight: 300;
    fill: var(--brand-blue);
    text-anchor: middle;
  }
  .brand-name {
    font-family: "Jost", sans-serif;
    font-weight: 700;
    font-size: 78px;
    fill: var(--brand-blue);
  }
  .brand-tagline {
    font-family: "Jost", sans-serif;
    font-weight: 400;
    font-size: 22px;
    fill: var(--tagline-ink);
  }
  .hero-field-top { stop-color: var(--sky-blue); }
  .hero-field-mid { stop-color: var(--brand-blue); }
  .hero-field-low { stop-color: var(--deep-navy); }
  .hero-field-base { stop-color: var(--night-violet); }
  .base-strip { fill: var(--night-violet); }
  .net-weight {
    font-family: "Josefin Sans", sans-serif;
    font-weight: 400;
    font-size: 31px;
    fill: var(--brand-blue);
    text-anchor: middle;
  }
</style>
</head>
<body>
<main class="bag-front">
  <svg class="bag-art" viewBox="0 0 918 1200" xmlns="http://www.w3.org/2000/svg">
    <defs>
      <linearGradient id="hero-field-fill" x1="0" y1="0" x2="0" y2="1">
        <stop class="hero-field-top" offset="0"/>
        <stop class="hero-field-mid" offset="0.25"/>
        <stop class="hero-field-low" offset="0.5"/>
        <stop class="hero-field-base" offset="0.75"/>
      </linearGradient>
    </defs>

    <g class="claim-badges">
      <g class="badge">
        <circle class="badge-ring" cx="82" cy="80" r="38"/>
        <text class="badge-label" x="82" y="76" font-size="13">40% LESS</text>
        <text class="badge-label" x="83" y="94" font-size="13">SODIUM</text>
      </g>
      <g class="badge">
        <circle class="badge-ring" cx="270" cy="80" r="38"/>
        <text class="badge-label" x="268" y="73" font-size="13">NO</text>
        <text class="badge-label" x="270" y="91" font-size="13">SUGAR</text>
        <line class="badge-slash" x1="296" y1="54" x2="245" y2="106"/>
      </g>
      <g class="badge">
        <circle class="badge-ring" cx="459" cy="80" r="38"/>
        <text class="badge-label" x="459" y="84" font-size="13">ALKALINE</text>
      </g>
      <g class="badge">
        <circle class="badge-ring" cx="647" cy="80" r="38"/>
        <text class="badge-label" x="645" y="75" font-size="13">NO</text>
        <text class="badge-label" x="647" y="93" font-size="13">FILLERS</text>
        <line class="badge-slash" x1="673" y1="54" x2="622" y2="106"/>
      </g>
      <g class="badge">
        <circle class="badge-ring" cx="836" cy="80" r="38"/>
        <text class="badge-label" x="834" y="76" font-size="10">NO</text>
        <text class="badge-label" x="836" y="90" font-size="9">FLAVOURINGS</text>
        <line class="badge-slash" x1="862" y1="54" x2="811" y2="106"/>
      </g>
    </g>

    <g class="brand-lockup">
      <text class="brand-name" x="203" y="270" textLength="526" lengthAdjust="spacingAndGlyphs">MARROW CREST</text>
      <text class="brand-tagline" x="203" y="297" textLength="526" lengthAdjust="spacing">Performance | Health | Taste</text>
    </g>

    <rect class="hero-field" x="179" y="334" width="560" height="727" fill="url(#hero-field-fill)"
          role="img" aria-label="Layered wave stripe artwork in sky blue, bright blue, red, navy and deep violet"/>

    <rect class="base-strip" x="0" y="1060" width="918" height="140"/>
    <text class="net-weight" x="462" y="1163">NET WT. 16 OZ.</text>
  </svg>
</main>
</body>
</html>
```